Business card for a "family office" company

Please provide professional looking business card designs, incorporating the attached logo and below details. Harrowmere Holdings Pty Ltd is a family office / financial investment company. We are looking for a modern, professional and contemporary card design.

Industry/Entity Type

Finance

Contact Information for Business Card

Name: Dean Malcott
Title: Director
Company: Harrowmere Holdings Pty Ltd
Email: harrowlead@ozmailnet.com.au
Mobile: 0492 635 718
Address: 3/412 Bramwood Parade, Marlowe Heights WA 6174, Australia

Requirements
Must have
• All details above and the logo. logo only on back side. incorporate colours of logo
Nice to have
• up to you
Should not have
• ?

```html
<!DOCTYPE html>
<html lang="en">
<head>
<meta charset="utf-8">
<title>Harrowmere Holdings – Business Card</title>
<link rel="stylesheet" href="https://fonts.googleapis.com/css2?family=Cinzel:wght@600&family=Roboto:wght@400;500;700&display=swap">
<style>
  :root {
    --page: #e3e3e3;
    --card: #f2f2f2;
    --navy: #1e1c57;
    --panel: #2a2960;
    --white: #ffffff;
  }
  * { margin: 0; padding: 0; box-sizing: border-box; }
  html, body { width: 1200px; height: 960px; overflow: hidden; background: var(--page); }
  .canvas { position: relative; width: 1200px; height: 960px; }

  .card { position: absolute; width: 600px; height: 343px; background: var(--card); overflow: hidden; }
  .card--front { left: 314px; top: 113px; }
  .card--back { left: 311px; top: 472px; }

  .brand-strip {
    position: absolute; left: 0; top: 0; width: 190px; height: 343px;
    display: flex; align-items: center; justify-content: center;
  }
  .brand-strip__name {
    transform: rotate(-90deg);
    font-family: "Cinzel", serif; font-weight: 600; color: var(--navy);
    font-size: 26px; line-height: 1.05; letter-spacing: 1px; text-align: center; white-space: nowrap;
  }

  .info-panel {
    position: absolute; left: 190px; top: 0; width: 410px; height: 343px;
    background: var(--panel); color: var(--white);
    font-family: "Roboto", sans-serif; text-align: center;
  }
  .info-panel__backdrop { position: absolute; inset: 0; width: 100%; height: 100%; }
  .info-panel__content { position: relative; padding-top: 67px; }
  .person-name { font-size: 27px; font-weight: 500; letter-spacing: 0; line-height: 32px; }
  .person-title { font-size: 15px; font-weight: 500; letter-spacing: 0.5px; margin-top: 2px; line-height: 20px; }
  .company-details { margin-top: 33px; font-size: 14.5px; line-height: 18.5px; }
  .company-details .company-name { font-weight: 500; }
  .contact-details { margin-top: 12px; font-size: 14.5px; line-height: 19.5px; }
  .contact-details b { font-weight: 700; }

  .back-brand {
    position: absolute; inset: 0; display: flex; flex-direction: column;
    align-items: center; justify-content: center; gap: 22px;
  }
  .back-brand__mark { width: 34px; height: 34px; background: var(--navy); }
  .back-brand__name {
    font-family: "Cinzel", serif; font-weight: 600; color: var(--navy);
    font-size: 34px; line-height: 1.1; letter-spacing: 2px; text-align: center;
  }
</style>
</head>
<body>
<main class="canvas">
  <section class="card card--front">
    <div class="brand-strip">
      <div class="brand-strip__name">HARROWMERE<br>HOLDINGS</div>
    </div>
    <div class="info-panel">
      <svg class="info-panel__backdrop" role="img" aria-label="Faint large brand symbol decoration in navy tones" viewBox="0 0 410 343" preserveAspectRatio="none">
        <rect width="410" height="343" fill="#2a2960"/>
      </svg>
      <div class="info-panel__content">
        <h1 class="person-name">DEAN MALCOTT</h1>
        <p class="person-title">DIRECTOR</p>
        <p class="company-details"><span class="company-name">Harrowmere Holdings Pty Ltd</span><br>3/412 Bramwood Parade<br>Marlowe Heights WA 6174, Australia</p>
        <p class="contact-details">
          <b>Phone:</b> 0492 635 718<br>
          <b>Email:</b> harrowlead@ozmailnet.com.au<br>
          <b>Web:</b> harrowmereholdings.com.au
        </p>
      </div>
    </div>
  </section>

  <section class="card card--back">
    <div class="back-brand">
      <div class="back-brand__mark"></div>
      <div class="back-brand__name">HARROWMERE<br>HOLDINGS</div>
    </div>
  </section>
</main>
</body>
</html>
```